Brindle kitchen designs

We are kitchen design company based in south Australia. We have high level of integrity and we believe strongly in what we do. Our aim is to put our clients in the driver seat, (it's your dream project not mine therefore your input is very important) which gives them control of their project, which we care about deeply.
We offer a detailed consultation, design package and or offer for a one of fee
to manage the project. We are also able to tender out the project to the local cabinet makers we work with. We are a service based company not a retail kitchen company. I like a matt black and a green which is what I gravitate to. The final design should convey integrity, quality with a strong belief in functional design.

Target Market(s)

both drawing for cabinet makers and the public more so the later

Contact Information for Business Card

logo with business name brindle kitchen design email gareth.pemberly@brindlekitchendesigns.com.au and mobile number 0427358162
appointment details at back of card.

Logo Text

brindle kitchen designs with the use of (bkd into the logo was my initial thought) open to your professional ideas.

Number of Pages Required

4 page

Font styles to use
Sans Serif
Other font styles liked:
• not sure a font to reflect info provided

Colors
9bcb3c

Requirements
Must have
• as above for business cards website page to flow through from that. Gallery pictures of kitchens etc. as with about us, contact page ' core home page. I need the easiest way to do a straight word press site with minimal plugins.
• I want what I have given you in the above info in project description to be on the website page, business cards and logo etc. I understand the logo is the core design element so this needs to he right. To have the proper colours & elements is also important.
Nice to have
• On website front page with logo in background perhaps. As i have mentioned in project description I want you to interpret that into of the project description so you can achieve the desired outcome.

```html
<!DOCTYPE html>
<html lang="en">
<head>
<meta charset="utf-8">
<title>Brindle Kitchen Designs</title>
<link href="https://fonts.googleapis.com/css2?family=Open+Sans:wght@400;600;700&family=Roboto+Condensed:wght@700&family=Roboto:wght@400&display=swap" rel="stylesheet">
<style>
:root{
  --green:#7cae25;
  --green-band:#86b52a;
  --green-light:#9bcb3c;
  --black:#222222;
  --ink:#333333;
  --white:#ffffff;
  --footer-bg:#f1f1f1;
}
*{margin:0;padding:0;box-sizing:border-box}
html,body{width:1200px;height:2442px;overflow:hidden}
body{position:relative;background:var(--white);font-family:"Open Sans",sans-serif;color:var(--ink)}
.abs{position:absolute}

/* header */
.site-header{left:0;top:0;width:1200px;height:82px;background:var(--white)}
.brand{left:99px;top:24px;font-family:"Roboto Condensed",sans-serif;font-weight:700;font-size:27px;line-height:34px;color:var(--green);white-space:nowrap}
.main-nav a{position:absolute;top:0;height:82px;line-height:82px;font-size:15px;color:#222;text-decoration:none;text-transform:uppercase}
.main-nav a.active{background:var(--green);color:var(--white);text-align:center;width:91px;left:474px}

/* hero */
.hero{left:0;top:82px;width:1200px;height:515px;background:linear-gradient(180deg,#4a4847 0%,#3a3938 55%,#4b4745 100%);overflow:hidden}
.hero-title{left:353px;top:207px;width:494px;height:81px;background:var(--green);color:var(--white);font-family:"Roboto Condensed",sans-serif;font-weight:700;font-size:41px;line-height:81px;text-align:center;white-space:nowrap}
.hero-text{left:190px;top:313px;width:820px;text-align:center;color:var(--white);font-weight:600;font-size:17px;line-height:34px}
.hero-arrow{top:206px}
.hero-cap{left:482px;top:480px;width:238px;height:80px;border-radius:50%;background:var(--white)}
.dots{display:flex;gap:4px}
.dots span{width:15px;height:15px;border-radius:50%;border:2px solid #444}
.dots span.on{background:var(--green);border-color:var(--green)}

/* about */
.section-title{font-family:"Roboto Condensed",sans-serif;font-weight:700;font-size:29px;color:var(--green)}
.rule{height:2px;background:var(--green)}
.about-text{left:99px;top:760px;width:620px;font-size:13px;line-height:26px;text-align:justify;color:#333}
.about-text p+p{margin-top:4px}
.btn{left:99px;top:949px;width:113px;height:46px;background:var(--green);color:var(--white);font-weight:700;font-size:15px;line-height:46px;text-align:center}
.about-drawing{left:754px;top:656px;width:446px;height:340px;background:linear-gradient(135deg,#f7f7f7,#e9e9e9)}

/* gallery */
.gallery{left:0;top:1053px;width:1200px;height:616px;background:linear-gradient(160deg,var(--green-light) 0%,var(--green-band) 60%,#7fae24 100%)}
.gallery-title{left:0;width:1200px;top:1095px;text-align:center;color:var(--white)}
.photo{border:3px solid var(--white)}
.gallery-dots span{border-color:var(--white)}
.gallery-dots span.on{background:var(--white)}

/* features */
.features{left:0;top:1669px;width:1200px;height:402px;background:var(--black)}
.feature-list{left:107px;top:1802px;width:560px;list-style:none;color:var(--white);font-family:"Roboto",sans-serif;font-size:16px;line-height:35px}
.feature-list li{position:relative;padding-left:26px}
.feature-list svg{position:absolute;left:0;top:9px}
.features-photo{left:697px;top:1724px;width:404px;height:292px;border:2px solid var(--white);background:linear-gradient(135deg,#d9d9d9 0%,#8a8a8a 45%,#2b2b2b 100%)}

/* footer */
.site-footer{left:0;top:2071px;width:1200px;height:371px;background:linear-gradient(135deg,#f5f5f5,#ececec)}
.footer-brand{left:99px;top:2207px;font-family:"Roboto Condensed",sans-serif;font-weight:700;font-size:26px;line-height:34px;color:var(--green);white-space:nowrap}
.footer-head{top:2108px;font-weight:700;font-size:19px;color:var(--green)}
.footer-nav{left:417px;top:2155px;list-style:none;font-size:14px;line-height:27.4px;color:#222}
.footer-nav li::before{content:"»";margin-right:12px;font-weight:700}
.social{left:648px;top:2160px;list-style:none;font-size:15px;color:#666}
.social li{height:36px;display:flex;align-items:center}
.social i{width:24px;height:24px;border-radius:50%;background:var(--green);margin-right:10px;display:inline-block}
.contact-item{left:874px;width:300px}
.contact-item .ring{position:absolute;left:0;top:0;width:38px;height:38px;border:2px solid var(--green);border-radius:50%;display:flex;align-items:center;justify-content:center}
.contact-item .label{position:absolute;left:54px;top:0;font-weight:700;font-size:14px;color:#222}
.contact-item .value{position:absolute;left:54px;top:22px;font-size:12.5px;line-height:20px;color:#333;width:220px}
.footer-line{left:99px;top:2382px;width:1002px;height:2px;background:#222}
.copyright{left:0;width:1200px;top:2400px;text-align:center;font-size:14px;color:#222}
</style>
</head>
<body>

<header class="site-header abs">
  <div class="brand abs">BRINDLE KITCHEN DESIGNS</div>
  <nav class="main-nav">
    <a class="active" href="#">Home</a>
    <a href="#" style="left:584px">Consultation</a>
    <a href="#" style="left:747px">Design Package</a>
    <a href="#" style="left:921px">Project</a>
    <a href="#" style="left:1029px">Contact</a>
  </nav>
</header>

<section class="hero abs" role="img" aria-label="Dim photo of a modern kitchen with wall shelves and timber cabinetry">
  <svg class="hero-arrow abs" style="left:24px" width="40" height="70" viewBox="0 0 40 70"><polyline points="34,2 4,35 34,68" fill="none" stroke="#fff" stroke-width="3"/></svg>
  <svg class="hero-arrow abs" style="left:1136px" width="40" height="70" viewBox="0 0 40 70"><polyline points="6,2 36,35 6,68" fill="none" stroke="#fff" stroke-width="3"/></svg>
  <div class="hero-cap abs"></div>
</section>
<h1 class="hero-title abs">BRINDLE KITCHEN DESIGN</h1>
<p class="hero-text abs">We are kitchen design company based in south Australia. We offer a detailed consultation, design package and or offer for a one of fee to manage the project.</p>
<div class="dots abs" style="left:554px;top:583px"><span class="on"></span><span></span><span></span><span></span><span></span></div>

<section class="about">
  <h2 class="section-title abs" style="left:99px;top:684px">About Brindle Kitchen Designs</h2>
  <div class="rule abs" style="left:99px;top:735px;width:199px"></div>
  <div class="about-text abs">
    <p>Nemo enim ipsam voluptatem quia voluptas sit aspernatur aut odit aut fugit, sed quia consequuntur magni dolores eos qui ratione voluptatem sequi nesciunt. Neque porro quisquam est, qui dolorem ipsum quia dolor sit amet, consectetur, adipisci velit, sed quia non numquam eius modi tempora incidunt ut labore et dolore magnam aliquam quaerat voluptatem.</p>
    <p>Nemo enim ipsam voluptatem quia voluptas sit aspernatur aut odit aut fugit, sed quia consequuntur magni dolores eos qui ratione voluptatem sequi nesciunt.</p>
  </div>
  <div class="btn abs">Read More</div>
  <div class="about-drawing abs" role="img" aria-label="Line drawing of a kitchen wall with cabinets, range hood and oven"></div>
</section>

<section class="gallery abs"></section>
<h2 class="section-title gallery-title abs">Our Gallery</h2>
<div class="rule abs" style="left:570px;top:1148px;width:60px;background:#fff"></div>
<div class="photo abs" style="left:39px;top:1241px;width:286px;height:270px;background:linear-gradient(135deg,#3a3a3a,#1c1c1c 60%,#5a4a32)" role="img" aria-label="Dark kitchen with black cabinets and warm under-cabinet lighting"></div>
<div class="photo abs" style="left:876px;top:1241px;width:286px;height:270px;background:linear-gradient(135deg,#c9bfb2,#8e7765 55%,#e6e2dc)" role="img" aria-label="Open plan kitchen and dining area with timber table"></div>
<div class="photo abs" style="left:322px;top:1205px;width:557px;height:342px;background:linear-gradient(160deg,#9a9a9a,#6c6c6c 50%,#4a3a2c)" role="img" aria-label="Grey kitchen with timber island and pendant lights"></div>
<div class="dots gallery-dots abs" style="left:552px;top:1607px"><span class="on"></span><span></span><span></span><span></span><span></span></div>

<section class="features abs"></section>
<h2 class="section-title abs" style="left:99px;top:1719px">Our Features</h2>
<div class="rule abs" style="left:99px;top:1767px;width:97px"></div>
<ul class="feature-list abs">
  <li><svg width="18" height="18" viewBox="0 0 18 18"><rect x="1" y="3" width="13" height="13" fill="none" stroke="#fff" stroke-width="1.6"/><polyline points="4,9 8,13 17,2" fill="none" stroke="#fff" stroke-width="2.2"/></svg>We are kitchen design company based in south Australia.</li>
  <li><svg width="18" height="18" viewBox="0 0 18 18"><rect x="1" y="3" width="13" height="13" fill="none" stroke="#fff" stroke-width="1.6"/><polyline points="4,9 8,13 17,2" fill="none" stroke="#fff" stroke-width="2.2"/></svg>We offer a detailed consultation, design package and or offer for a one of fee to manage the project.</li>
  <li><svg width="18" height="18" viewBox="0 0 18 18"><rect x="1" y="3" width="13" height="13" fill="none" stroke="#fff" stroke-width="1.6"/><polyline points="4,9 8,13 17,2" fill="none" stroke="#fff" stroke-width="2.2"/></svg>We are also able to tender out the project to the local cabinet makers we work with.</li>
  <li><svg width="18" height="18" viewBox="0 0 18 18"><rect x="1" y="3" width="13" height="13" fill="none" stroke="#fff" stroke-width="1.6"/><polyline points="4,9 8,13 17,2" fill="none" stroke="#fff" stroke-width="2.2"/></svg>We are a service based company not a retail kitchen company.</li>
</ul>
<div class="features-photo abs" role="img" aria-label="Black and white kitchen with island, range hood and bar stools"></div>

<footer class="site-footer abs"></footer>
<div class="footer-brand abs">BRINDLE KITCHEN DESIGNS</div>
<h3 class="footer-head abs" style="left:417px">NAVIGATION</h3>
<h3 class="footer-head abs" style="left:648px">GET SOCIAL</h3>
<h3 class="footer-head abs" style="left:874px">CONTACT US</h3>
<ul class="footer-nav abs">
  <li>Home</li><li>Consultation</li><li>Design Package</li><li>Project</li><li>Gallery</li><li>Contact Us</li>
</ul>
<ul class="social abs">
  <li><i></i>Circlebook</li><li><i></i>Chirper</li><li><i></i>Searchly+</li><li><i></i>Linkwork</li><li><i></i>ViewTube</li>
</ul>
<div class="contact-item abs" style="top:2164px">
  <div class="ring"><svg width="14" height="18" viewBox="0 0 14 18"><path d="M7 1a6 6 0 0 0-6 6c0 4.5 6 10 6 10s6-5.5 6-10a6 6 0 0 0-6-6z" fill="none" stroke="#7cae25" stroke-width="1.6"/><circle cx="7" cy="7" r="2" fill="#7cae25"/></svg></div>
  <div class="label">Address:</div>
  <div class="value">Marlow Heights, Eastvale,<br>SA, 5093</div>
</div>
<div class="contact-item abs" style="top:2241px">
  <div class="ring"><svg width="10" height="16" viewBox="0 0 10 16"><rect x="1" y="1" width="8" height="14" rx="1.5" fill="none" stroke="#7cae25" stroke-width="1.6"/><circle cx="5" cy="12.3" r="1" fill="#7cae25"/></svg></div>
  <div class="label">PHONE:</div>
  <div class="value">180 047 913</div>
</div>
<div class="contact-item abs" style="top:2301px">
  <div class="ring"><svg width="16" height="12" viewBox="0 0 16 12"><rect x="1" y="1" width="14" height="10" fill="#7cae25"/><polyline points="1,1 8,7 15,1" fill="none" stroke="#fff" stroke-width="1.3"/></svg></div>
  <div class="label">EMAIL:</div>
  <div class="value">info@brindlekitchendesigns.com</div>
</div>
<div class="footer-line abs"></div>
<p class="copyright abs">© 2017 Brindle Kitchen Designs. All Rights Reserved.</p>

</body>
</html>
```